Redesign of the Molvekraut label

I am a pharmacist and sell a bitters called "Molvekraut". I would like to revise and modernize the current logo of my "Molvekraut". I have attached a photo of the current label. I have different bottle sizes with different label sizes, but for now I will only need one label for the 700ml size:
20ml 36x47mm
40ml 45x62mm
200ml 70x91mm
350ml 70x98mm
500ml 70x110mm
700ml 87x119mm
The Molve is a small stream that runs through our town. The Molvekraut is a play on words that takes up the mysticism of the Harz, as a spirit can of course also be a schnapps. I like the mysticism and rough nature of the Harz in connection with the product. I have attached a logo suggestion that I once had an AI design. But I am very open to new ideas. A connection to my pharmacy does not necessarily have to be recognizable. VG, K. Harmsen

Target Market(s)

End consumers, gastronomy, restaurants, hotels

```html
<!DOCTYPE html>
<html lang="de">
<head>
<meta charset="utf-8">
<title>Molvekraut – Molvetaler Kräuterbitter Etikett 700ml</title>
<link rel="stylesheet" href="https://fonts.googleapis.com/css2?family=Anton&family=Cutive&family=Fira+Sans+Condensed:wght@700&family=Rokkitt:wght@800&display=swap">
<style>
  :root {
    --ink: #0e0d0c;
    --tan: #c99a6b;
    --paper: #ffffff;
    --stage: #f2f0ec;
  }
  * { margin: 0; padding: 0; box-sizing: border-box; }
  html, body { width: 1200px; height: 866px; overflow: hidden; background: var(--stage); }
  .canvas { position: relative; width: 1200px; height: 866px; }
  .label-frame { position: absolute; left: 307px; top: 33px; width: 585px; height: 800px; }
  .label {
    position: absolute; left: 0; top: 0; width: 877px; height: 1200px;
    transform: scale(0.6667); transform-origin: 0 0;
    border-radius: 110px; overflow: hidden; background: var(--ink);
  }
  .label-art { position: absolute; inset: 0; }

  .brand { position: absolute; left: 60px; top: 70px; width: 260px; text-align: center; }
  .brand-dot { display: block; width: 110px; height: 110px; margin: 0 auto 24px; border-radius: 50%; background: var(--paper); }
  .brand-name { font-family: "Rokkitt", serif; font-weight: 800; font-size: 40px; letter-spacing: 3px; color: var(--paper); }

  .product-name {
    position: absolute; left: 0; top: 300px; width: 877px; height: 170px;
    text-align: center; white-space: nowrap;
    font-family: "Anton", sans-serif; font-weight: 400; font-size: 140px; line-height: 170px;
    letter-spacing: 2px; color: var(--ink);
  }
  .grade {
    position: absolute; left: 599px; top: 212px; width: 220px; text-align: center;
    font-family: "Fira Sans Condensed", sans-serif; font-weight: 700; font-size: 34px; color: var(--ink);
  }

  .subtitle {
    position: absolute; left: 60px; top: 510px; width: 757px; text-align: center;
    font-family: "Rokkitt", serif; font-weight: 800; font-size: 38px; line-height: 42px;
    letter-spacing: 1.5px; color: var(--tan);
  }
  .description {
    position: absolute; left: 70px; top: 615px; width: 737px; text-align: center;
    font-family: "Cutive", serif; font-size: 25px; line-height: 42px; color: var(--paper);
  }

  .footer { position: absolute; left: 0; top: 903px; width: 877px; height: 297px; background: var(--tan); color: var(--ink); }
  .pharmacy-mark { position: absolute; left: 86px; top: 40px; width: 114px; height: 114px; border: 4px solid var(--ink); border-radius: 50%; }
  .pharmacy, .maker {
    position: absolute; top: 28px; text-align: center;
    font-family: "Rokkitt", serif; font-weight: 800; font-size: 30px; line-height: 32px; letter-spacing: 1px;
  }
  .pharmacy { left: 206px; width: 220px; }
  .pharmacy .lead { font-family: "Cutive", serif; font-weight: 400; font-size: 25px; letter-spacing: 0; }
  .maker { left: 460px; width: 360px; }
  .volume { position: absolute; left: 0; top: 186px; width: 877px; text-align: center; font-family: "Rokkitt", serif; font-weight: 800; font-size: 30px; letter-spacing: 1px; }
  .legal { position: absolute; left: 0; top: 236px; width: 877px; text-align: center; font-family: "Rokkitt", serif; font-weight: 800; font-size: 22px; letter-spacing: 0.5px; }
</style>
</head>
<body>
<main class="canvas">
  <div class="label-frame">
    <article class="label">
      <svg class="label-art" width="877" height="1200" viewBox="0 0 877 1200" aria-hidden="true">
        <g fill="none" stroke="var(--tan)">
          <path class="frame-line-outer" stroke-width="7" d="M23 903 V113 A90 90 0 0 1 113 23 H764 A90 90 0 0 1 854 113 V903"/>
          <path class="frame-line-inner" stroke-width="3" d="M38 903 V114 A76 76 0 0 1 114 38 H763 A76 76 0 0 1 839 114 V903"/>
        </g>
        <rect class="title-band" fill="var(--tan)" x="0" y="300" width="877" height="170"/>
        <polygon class="grade-ribbon" fill="var(--paper)" points="599,195 819,195 819,290 709,268 599,290"/>
      </svg>

      <div class="brand">
        <span class="brand-dot"></span>
        <span class="brand-name">MOLVEKRAUT</span>
      </div>

      <p class="grade">FEINSTER</p>
      <h1 class="product-name">MOLVETALER</h1>

      <h2 class="subtitle">Kräuterbitter<br>nach überliefertem Rezept</h2>
      <p class="description">
        Sorgsam bereitet nach einer Rezeptur,<br>
        die seit jeher gut gehütet wird. Ein feiner<br>
        Abschluss jeder Mahlzeit.<br>
        Vollendet mit Auszügen aus Enzianwurzel,<br>
        Pomeranze, Galgant, Wermut und weiteren<br>
        edlen Kräutern des Harzes.
      </p>

      <footer class="footer">
        <span class="pharmacy-mark"></span>
        <p class="pharmacy"><span class="lead">Aus der</span><br>ST. LORENZ<br>APOTHEKE<br>MOLVETAL</p>
        <p class="maker">DR. K. HARMSEN<br>BRUNNENWEG 12<br>38001 MOLVETAL,<br>TEL. 05500-1234</p>
        <p class="volume">700ML 34% VOL</p>
        <p class="legal">BITTERLIKÖR MIT CHININ L4807152</p>
      </footer>
    </article>
  </div>
</main>
</body>
</html>
```